Free Offer Book Cover

I am creating a funnel page where I offer a free download of a PDF called. Twelve-Week Launch Kit. A road map for new leaders. I have included samples of other book covers. It can look like a book, or a checklist, or something that illustrates what they are getting. Bright Harbor Coaching is the company if you could get the logo into the book cover as well.

Target Market(s)

New leaders, young professionals

Font styles to use
Sans Serif

Requirements
Must have
• Name of content. Twelve-Week Launch Kit for new leaders.

```html
<!DOCTYPE html>
<html lang="en">
<head>
<meta charset="utf-8">
<title>Twelve-Week Launch Kit – Cover</title>
<link rel="stylesheet" href="https://fonts.googleapis.com/css2?family=Archivo+Black&family=Oswald:wght@500;600&display=swap">
<style>
  :root {
    --backdrop: #cccccc;
    --cover-black: #1b1b1b;
    --accent-red: #f0222e;
    --text-white: #f4f4f4;
  }
  * { margin: 0; padding: 0; box-sizing: border-box; }
  html, body {
    width: 1200px;
    height: 900px;
    overflow: hidden;
    background: var(--backdrop);
  }
  .canvas {
    width: 1200px;
    height: 900px;
    display: flex;
    align-items: center;
    justify-content: center;
  }
  .book-cover {
    width: 540px;
    height: 800px;
    background: var(--cover-black);
    display: flex;
    flex-direction: column;
    align-items: center;
    padding: 120px 56px 0;
    box-shadow: 0 18px 40px rgba(0,0,0,0.25);
  }
  .title-kicker {
    display: flex;
    align-items: center;
    gap: 22px;
    width: 100%;
  }
  .title-kicker .rule {
    flex: 1;
    height: 12px;
    background: var(--accent-red);
  }
  .title-kicker .word {
    font-family: "Archivo Black", sans-serif;
    font-size: 52px;
    line-height: 1;
    color: var(--accent-red);
    letter-spacing: 1px;
  }
  .title-main {
    font-family: "Archivo Black", sans-serif;
    font-size: 132px;
    line-height: 1;
    color: var(--accent-red);
    margin-top: 6px;
  }
  .title-sub {
    font-family: "Oswald", sans-serif;
    font-weight: 600;
    font-size: 68px;
    line-height: 1;
    color: var(--text-white);
    letter-spacing: 2px;
    margin-top: 10px;
  }
  .brand {
    display: flex;
    align-items: center;
    gap: 12px;
    margin-top: 58px;
  }
  .brand .mark {
    width: 16px;
    height: 16px;
    background: var(--accent-red);
  }
  .brand .name {
    font-family: "Oswald", sans-serif;
    font-weight: 500;
    font-size: 26px;
    color: var(--text-white);
    letter-spacing: 3px;
    text-transform: uppercase;
  }
  .divider {
    width: 100%;
    height: 10px;
    background: var(--accent-red);
    margin-top: 90px;
  }
  .tagline {
    font-family: "Oswald", sans-serif;
    font-weight: 500;
    font-size: 33px;
    color: var(--accent-red);
    letter-spacing: 1px;
    text-transform: uppercase;
    margin-top: 18px;
  }
</style>
</head>
<body>
  <main class="canvas">
    <section class="book-cover">
      <div class="title-kicker">
        <span class="rule"></span>
        <span class="word">TWELVE</span>
        <span class="rule"></span>
      </div>
      <h1 class="title-main">WEEK</h1>
      <p class="title-sub">LAUNCH KIT</p>
      <div class="brand">
        <span class="mark"></span>
        <span class="name">Bright Harbor Coaching</span>
      </div>
      <div class="divider"></div>
      <p class="tagline">A Road Map for New Leaders</p>
    </section>
  </main>
</body>
</html>
```